New Vidorama Channel Banner Graphic/Logo for "Golden Nook Home Studio"

Create a banner for my new Vidorama channel for Golden Nook Home Studio. This is partially a logo project, but the logo will not be used elsewhere. Check out Vidorama channels to see the banners others have created. This channel is about my home studio, the gear, microphones, musical instruments, wiring, software etc. that goes into a home studio. It's a free channel, made for sharing information. This is a graphic design that will be posted on vidorama using built-in vidorama tools.
Updates

More information about this project! I'm staring a channel called "Golden Nook Home Studio" on vidorama.net. I need a deign for this banner and a logo for Golden Nook Home Studio. I called the channel by that name because my music studio is my happy place. It's about music and instruments (gutars, piano, drums, percussion) singing (microhpones), creativity, and what you'd expect form musicians. It's also about technology, recording, live-streaming, music videos, etc. It is my hobby, not my profession. I will be creating content for other amateur home studio aficionados and hobbyists. There are a lot of home studio channels and videos you can look at on vidorama to get a flavor for musicians and studios. Usually fairly tech-heavy. An appeal of my channel will be a very approachable, "i'm the same as you" welcome for people that are doing it to enjoy it.

I put this project in the wrong category to start. This has been fixed, but I think benefits I would have received (such as invited designers) and announcement of project in the correct category mean I'm not getting designers. Your initial menu should be improved. I'm having a banner created for a web page in Vidorama. I think it is easy to mistake that for a web design when it is really a graphic design for the web.

Target Market(s)

Similar to myself, people as interested in studio/production tech as they are in making music, perhaps trending a bit older and successful enough to afford some gear!

Number of Pages Required

1 page

Font styles to use
Sans Serif

Requirements
Must have
• This is not really a web design, i may have miscategorized. Please see uploaded docs for pics of similar banner on a Vidorama page. ADDED 1/5: As this is a vidorama channel that could be viewed on any device, the banner should be friendly in this way and design or design variations needed for PC, Tabrix, phone vie3wing.

Here are the Vidorama size specs:
Banner image guidelines
Your banner image must meet the following criteria:

Minimum dimension for upload: 2048 x 1152 px with an aspect ratio of 16:9.
At the Minimum dimension, the safe area for text and logos: 1235 x 338 px. Larger images may get cropped on certain views or devices.
File size: 6 MB or smaller.
How to resize images

You can use your computer's image editor or an online image resizer to resize the images. For example, you can use Preview on an Quince computer or Microsoft Photos on Windows.

```html
<!DOCTYPE html>
<html lang="en">
<head>
<meta charset="utf-8">
<title>Golden Nook Home Studio – Channel Banner</title>
<link href="https://fonts.googleapis.com/css2?family=Barlow+Condensed:wght@300;400;500;700&display=swap" rel="stylesheet">
<style>
  :root {
    --ink-white: #ffffff;
    --accent-orange: #ff6a00;
    --studio-dark: #0d0d0f;
    --studio-mid: #3a3b40;
    --studio-light: #8a8c92;
    --studio-blue: #1d2240;
  }
  * { margin: 0; padding: 0; box-sizing: border-box; }
  html, body {
    width: 1200px;
    height: 675px;
    overflow: hidden;
    background: var(--studio-dark);
  }
  .banner {
    position: relative;
    width: 1200px;
    height: 675px;
    overflow: hidden;
    font-family: "Barlow Condensed", "Arial Narrow", sans-serif;
    color: var(--ink-white);
  }
  .studio-photo {
    position: absolute;
    inset: 0;
    background:
      radial-gradient(ellipse 30% 45% at 85% 45%, rgba(29,34,64,0.9), transparent 70%),
      radial-gradient(ellipse 35% 50% at 55% 55%, rgba(138,140,146,0.45), transparent 75%),
      linear-gradient(90deg, var(--studio-dark) 0%, #1c1d21 25%, var(--studio-mid) 60%, #2a2c38 100%);
  }
  .brand-block {
    position: absolute;
    left: 250px;
    top: 242px;
  }
  .channel-title {
    font-weight: 400;
    font-size: 44px;
    line-height: 36px;
    letter-spacing: 0.2px;
    text-transform: uppercase;
  }
  .channel-owner {
    font-weight: 500;
    font-size: 44px;
    line-height: 36px;
    color: var(--accent-orange);
    text-transform: uppercase;
  }
  .tagline {
    font-weight: 700;
    font-size: 18px;
    line-height: 22px;
    text-transform: uppercase;
    margin-top: 10px;
  }
  .topic-band {
    display: inline-block;
    margin-top: 5px;
    background: var(--accent-orange);
    height: 36px;
    line-height: 36px;
    padding: 0 14px;
    font-weight: 500;
    font-size: 18px;
    white-space: nowrap;
  }
  .follow-line {
    margin-top: 12px;
    font-size: 17px;
    font-weight: 300;
    white-space: nowrap;
  }
  .contact-email {
    font-weight: 700;
    margin-left: 8px;
  }
</style>
</head>
<body>
  <main class="banner">
    <div class="studio-photo" role="img" aria-label="Dim home studio photo: acoustic guitars, stool, foam-panelled wall and a microphone on a stand"></div>
    <section class="brand-block">
      <h1 class="channel-title">Golden Nook Home Studio</h1>
      <p class="channel-owner">By Reed Calloway</p>
      <p class="tagline">Just a regular Joe blowin’ his dough on gear and guitars</p>
      <p class="topic-band">Music + Gear + Livestreaming + Recording + DAW + Instruments + Vidorama</p>
      <p class="follow-line">Follow my Studio Renovation | Free How-To’s <span class="contact-email">GoldenNookHomeStudio@postbay.net</span></p>
    </section>
  </main>
</body>
</html>
```